Swimming Pool Business Billboard

10' x 24' Billboard displaying company name, logo and phone number. Picture of swimming pool activity; kids playing , swimming, etc. Bullet points possibly shown: New Construction, Repairs, Weekly maintenance.

Industry/Entity Type

Swimming pool construction, repairs and maintenance.

Font styles to use
Sans Serif

Colors
0054AA
0677BA
7BADD7
CADEEF
E8F1F8

Requirements
Must have
• Rusty & Calder Pembrook, RUSTY'S POOLS & Service,
Nice to have
• Prefer to have my last name "Pembrook" above the word "POOLS" only in smaller print so that "RUSTYS POOLS" is distinguished.

```html
<!DOCTYPE html>
<html lang="en">
<head>
<meta charset="UTF-8">
<title>Rusty's Pools &amp; Service – Billboard</title>
<link rel="stylesheet" href="https://fonts.googleapis.com/css2?family=Roboto+Slab:wght@400;800;900&family=Montserrat:wght@800&family=Poppins:wght@400;600&display=swap">
<style>
  :root {
    --navy: #1b3a6b;
    --cyan: #0cb4ea;
    --ink: #0d0d12;
    --white: #ffffff;
    --canvas: #ffffff;
    --water-deep: #3f9bd3;
    --water-mid: #6fbde6;
    --water-bright: #a9dbf3;
    --water-light: #cadeef;
    --shadow: rgba(0, 0, 0, 0.28);
  }
  * { margin: 0; padding: 0; box-sizing: border-box; }
  html, body {
    width: 1071px;
    height: 1200px;
    overflow: hidden;
    background: var(--canvas);
  }
  .billboard {
    position: absolute;
    left: 48px;
    top: 397px;
    width: 975px;
    height: 405px;
    background: var(--white);
    box-shadow: 0 4px 14px var(--shadow);
    overflow: hidden;
  }
  .owners {
    position: absolute;
    left: 25px;
    top: 34px;
    font: 400 23px/1 "Roboto Slab", serif;
    color: var(--navy);
    white-space: nowrap;
  }
  .headline {
    position: absolute;
    left: 23px;
    top: 68px;
    font-family: "Roboto Slab", serif;
    font-weight: 900;
    font-size: 48px;
    line-height: 51px;
    white-space: nowrap;
  }
  .headline .brand { color: var(--navy); display: block; }
  .headline .service { color: var(--cyan); display: block; font-weight: 800; }
  .accent-rule {
    position: absolute;
    left: 25px;
    top: 175px;
    width: 55px;
    height: 4px;
    background: var(--cyan);
  }
  .services {
    position: absolute;
    left: 25px;
    top: 205px;
    list-style: none;
    font: 800 26px/32.5px "Montserrat", sans-serif;
    color: var(--ink);
    white-space: nowrap;
  }
  .services li::before {
    content: "";
    display: inline-block;
    width: 8px;
    height: 8px;
    border-radius: 50%;
    background: var(--cyan);
    margin: 0 13px 5px 0;
    vertical-align: middle;
  }
  .mark {
    position: absolute;
    left: 440px;
    top: 20px;
    width: 210px;
    height: 300px;
    display: flex;
    flex-direction: column;
    align-items: center;
    justify-content: center;
    gap: 14px;
    font: 900 40px/1.05 "Roboto Slab", serif;
    color: var(--navy);
    text-align: center;
  }
  .mark .dot {
    width: 70px;
    height: 70px;
    border-radius: 50%;
    background: var(--navy);
  }
  .pool-photo {
    position: absolute;
    left: 655px;
    top: 0;
    width: 320px;
    height: 336px;
    background:
      linear-gradient(90deg, var(--white) 0%, rgba(255,255,255,0) 12%),
      radial-gradient(ellipse at 60% 45%, var(--water-bright) 0%, rgba(169,219,243,0) 55%),
      linear-gradient(180deg, var(--water-mid) 0%, var(--water-deep) 50%, var(--water-mid) 78%, var(--water-light) 100%);
  }
  .contact-bar {
    position: absolute;
    left: 0;
    top: 336px;
    width: 975px;
    height: 69px;
    background: var(--navy);
    color: var(--white);
    font-family: "Poppins", sans-serif;
  }
  .contact {
    position: absolute;
    top: 0;
    height: 69px;
    display: flex;
    align-items: center;
    gap: 5px;
    white-space: nowrap;
  }
  .contact svg { flex: none; }
  .contact.phone { left: 23px; font-weight: 600; font-size: 33px; }
  .contact.email { left: 292px; font-size: 21px; }
  .contact.address { left: 574px; font-size: 20px; }
</style>
</head>
<body>
  <main class="billboard">
    <p class="owners">Rusty &amp; Calder Pembrook</p>
    <h1 class="headline">
      <span class="brand">RUSTY'S POOLS</span>
      <span class="service">&amp; SERVICE</span>
    </h1>
    <div class="accent-rule"></div>
    <ul class="services">
      <li>NEW CONSTRUCTION</li>
      <li>REPAIRS &amp; MAINTENANCE</li>
      <li>WEEKLY MAINTENANCE</li>
    </ul>

    <div class="mark"><span class="dot"></span><span>RUSTY'S<br>POOLS</span></div>

    <div class="pool-photo" role="img" aria-label="Photo of a smiling child in goggles at the edge of a bright blue swimming pool with a lane rope behind"></div>

    <footer class="contact-bar">
      <div class="contact phone">
        <svg width="20" height="20" viewBox="0 0 20 20" aria-hidden="true">
          <circle cx="10" cy="10" r="10" fill="var(--cyan)"/>
          <path d="M6.5 5.5l2 -0.5 1 2.3 -1.2 1c.6 1.3 1.6 2.3 2.9 2.9l1-1.2 2.3 1-.5 2c-4.2.2-7.7-3.3-7.5-7.5z" fill="var(--white)"/>
        </svg>
        555-204-1187
      </div>
      <div class="contact email">
        <svg width="20" height="20" viewBox="0 0 20 20" aria-hidden="true">
          <circle cx="10" cy="10" r="10" fill="var(--cyan)"/>
          <rect x="5" y="6.5" width="10" height="7" fill="none" stroke="var(--white)" stroke-width="1.2"/>
          <path d="M5 6.5l5 4 5-4" fill="none" stroke="var(--white)" stroke-width="1.2"/>
        </svg>
        rusty@rcpools.net
      </div>
      <div class="contact address">
        <svg width="20" height="20" viewBox="0 0 20 20" aria-hidden="true">
          <circle cx="10" cy="10" r="10" fill="var(--cyan)"/>
          <path d="M10 15.5s-4-4-4-7a4 4 0 0 1 8 0c0 3-4 7-4 7z" fill="none" stroke="var(--white)" stroke-width="1.3"/>
          <circle cx="10" cy="8.5" r="1.4" fill="var(--white)"/>
        </svg>
        2270 Marlow Ln Fernhill, GA 30199
      </div>
    </footer>
  </main>
</body>
</html>
```